Falcrest security business card

Looking for a business card for my security company

Target Market(s)

Security

Industry/Entity Type

Security

Contact Information for Business Card

Name - Gil Marston. Title - General manager - direct 314 862.4490 website www. falcrestsecurityservices.example email - gil@ falcrestsecurityservices.example

Requirements
Must have
• Logo attached

```html
<!DOCTYPE html>
<html lang="en">
<head>
<meta charset="utf-8">
<title>Falcrest Security Services – Business Card</title>
<link href="https://fonts.googleapis.com/css2?family=Arimo:wght@400;700&display=swap" rel="stylesheet">
<style>
  :root {
    --stage: #c4c3c4;
    --ink: #0a0909;
    --gold-light: #f8f0c6;
    --gold-mid: #d9b56e;
    --gold-deep: #b27f33;
    --gold-text: #d6ac5c;
    --text-dark: #111111;
  }
  html, body {
    margin: 0;
    padding: 0;
    width: 1200px;
    height: 1200px;
    overflow: hidden;
    background: var(--stage);
    font-family: "Arimo", Arial, sans-serif;
  }
  .card {
    position: absolute;
    left: 191px;
    width: 819px;
    height: 467px;
    background: var(--ink);
    box-shadow: 0 1px 3px rgba(0,0,0,0.35);
    overflow: hidden;
  }
  .card--front { top: 102px; }
  .card--back { top: 630px; }
  .card__art {
    position: absolute;
    inset: 0;
    width: 100%;
    height: 100%;
  }
  .brand {
    position: absolute;
    color: var(--gold-text);
    font-weight: 700;
    letter-spacing: 2px;
    text-transform: uppercase;
    display: flex;
    align-items: center;
    gap: 14px;
    white-space: nowrap;
  }
  .brand__dot {
    width: 18px;
    height: 18px;
    border-radius: 50%;
    background: var(--gold-text);
  }
  .card--front .brand {
    left: 380px;
    top: 112px;
    font-size: 52px;
  }
  .card--back .brand {
    left: 0;
    right: 0;
    top: 196px;
    justify-content: center;
    font-size: 62px;
  }
  .contact {
    position: absolute;
    left: 49px;
    top: 268px;
    color: var(--text-dark);
  }
  .contact__name {
    margin: 0;
    font-size: 26px;
    font-weight: 700;
    line-height: 1.1;
  }
  .contact__title {
    margin: 3px 0 0;
    font-size: 19px;
    font-weight: 400;
  }
  .contact__list {
    list-style: none;
    margin: 22px 0 0;
    padding: 0;
    font-size: 19px;
    line-height: 27px;
  }
  .contact__list li {
    display: flex;
    align-items: center;
    gap: 13px;
  }
  .contact__icon {
    width: 16px;
    height: 16px;
    flex: none;
  }
  .card__band {
    position: absolute;
    left: 0;
    right: 0;
    bottom: 0;
    height: 13px;
    background: linear-gradient(90deg, var(--gold-deep), var(--gold-mid) 25%, var(--gold-light) 38%, var(--gold-deep) 55%, var(--gold-light) 75%, var(--gold-mid) 88%, var(--gold-deep));
  }
</style>
</head>
<body>

<section class="card card--front" aria-label="Card front">
  <svg class="card__art" viewBox="0 0 819 467" preserveAspectRatio="none" aria-hidden="true">
    <defs>
      <linearGradient id="goldField" x1="0" y1="0" x2="0.6" y2="1">
        <stop offset="0" stop-color="#f9f2c8"/>
        <stop offset="0.5" stop-color="#d7b470"/>
        <stop offset="1" stop-color="#b27f33"/>
      </linearGradient>
      <linearGradient id="goldSwoosh" x1="0" y1="0" x2="1" y2="1">
        <stop offset="0" stop-color="#b27f33"/>
        <stop offset="0.5" stop-color="#d9b56e"/>
        <stop offset="0.8" stop-color="#fbf3cc"/>
        <stop offset="1" stop-color="#c48f3e"/>
      </linearGradient>
    </defs>
    <path d="M0 0 H290 C230 60 240 150 330 210 C450 270 620 320 665 390 C680 420 640 450 610 467 H0 Z" fill="url(#goldSwoosh)"/>
    <path d="M0 0 H268 C215 50 230 140 320 205 C430 265 610 320 640 385 C655 420 620 450 590 467 H0 Z" fill="url(#goldField)"/>
    <path d="M226 118 C250 200 360 240 470 285 C580 330 650 360 660 420 C662 440 640 455 620 467" fill="none" stroke="#f7ecbf" stroke-width="3" opacity="0.8"/>
  </svg>

  <div class="brand"><span class="brand__dot"></span>Falcrest</div>

  <div class="contact">
    <h1 class="contact__name">GIL MARSTON</h1>
    <p class="contact__title">General manager</p>
    <ul class="contact__list">
      <li>
        <svg class="contact__icon" viewBox="0 0 16 16" aria-hidden="true"><path d="M3 1.5 L6 1 L7.5 4.5 L5.6 6 C6.4 7.8 8.2 9.6 10 10.4 L11.5 8.5 L15 10 L14.5 13 C14.3 14.2 13 15 11.8 14.8 C6.5 14 2 9.5 1.2 4.2 C1 3 1.8 1.7 3 1.5 Z" fill="#111"/></svg>
        <span>314 862.4490</span>
      </li>
      <li>
        <svg class="contact__icon" viewBox="0 0 16 16" aria-hidden="true"><rect x="1" y="3" width="14" height="10" rx="1" fill="none" stroke="#111" stroke-width="1.4"/><path d="M1.5 3.5 L8 9 L14.5 3.5" fill="none" stroke="#111" stroke-width="1.4"/></svg>
        <span>gil@falcrestsecurityservices.example</span>
      </li>
      <li>
        <svg class="contact__icon" viewBox="0 0 16 16" aria-hidden="true"><g fill="none" stroke="#111" stroke-width="1.2"><circle cx="8" cy="8" r="6.8"/><ellipse cx="8" cy="8" rx="3" ry="6.8"/><path d="M1.2 8 H14.8 M2.2 4.6 H13.8 M2.2 11.4 H13.8 M8 1.2 V14.8"/></g></svg>
        <span>www.falcrestsecurityservices.example</span>
      </li>
    </ul>
  </div>
</section>

<section class="card card--back" aria-label="Card back">
  <div class="brand"><span class="brand__dot"></span>Falcrest</div>
  <div class="card__band"></div>
</section>

</body>
</html>
```